Plakat-Design für Vogelvolieren
Zielgruppe
Es geht um vier Din A4-Plakate, die an vier Vogelvolieren hängen und Informationen zu den Vögeln bieten, die sich in den Volieren befinden.
Die Volieren gehören zum Wildpark Kernbachtal. Einem kleinen Wildpark, bei dem ausschließlich Ehrenamtliche tätig sind. Der Eintritt ist frei.
Die Zielgruppe sind die Besucher - von klein bis groß, von jung bis alt
Aufgabenstellung
Gute Lesbarkeit, denn die Informationsvermittlung soll im Vordergrund stehen.
Wir benötigen 1 Plakatdesign und die offenen Daten in InDesign, denn dann würden wir bei den weiteren drei Plakaten die Texte und Fotos austauschen.
Es sind 2 Plakate mit 4 Vögeln und 2 Plakate mit 2 Vögeln.

```html
<!DOCTYPE html>
<html lang="de">
<head>
<meta charset="utf-8">
<title>Unzertrennliche – Wildpark Kernbachtal</title>
<link href="https://fonts.googleapis.com/css2?family=Source+Sans+3:wght@400;600;700&family=Source+Serif+4:opsz,wght@8..60,700;8..60,800&display=swap" rel="stylesheet">
<style>
  :root {
    --page: #ffffff;
    --cream: #fdf0df;
    --orange: #e59a45;
    --orange-text: #e0913c;
    --ink: #2a2a2a;
    --wood-light: #e9b678;
    --wood-mid: #d69b56;
    --wood-dark: #c0823f;
  }
  html, body {
    margin: 0;
    width: 1200px;
    height: 960px;
    overflow: hidden;
    background: var(--page);
  }
  .poster {
    position: absolute;
    left: 88px;
    top: 118px;
    width: 1029px;
    height: 728px;
    background: var(--cream);
    box-shadow: 0 2px 14px rgba(0,0,0,0.12);
    font-family: "Source Sans 3", sans-serif;
    color: var(--ink);
  }
  .photo {
    position: absolute;
    left: 0; top: 0;
    width: 582px; height: 623px;
    background: linear-gradient(170deg, var(--wood-light) 0%, var(--wood-mid) 30%, var(--wood-light) 55%, var(--wood-dark) 100%);
  }
  .title-box {
    position: absolute;
    left: 0; top: 529px;
    width: 548px; height: 73px;
    background: var(--cream);
    display: flex;
    align-items: center;
    padding-left: 38px;
    box-sizing: border-box;
  }
  .title {
    margin: 0;
    font-weight: 700;
    font-size: 52px;
    letter-spacing: 1.5px;
    color: var(--orange);
    line-height: 1;
  }
  .info {
    position: absolute;
    left: 582px; top: 0;
    width: 447px; height: 623px;
  }
  .brand {
    position: absolute;
    left: 70px; top: 88px;
    display: flex;
    align-items: center;
    gap: 12px;
  }
  .brand-dot {
    width: 20px; height: 20px;
    border-radius: 50%;
    background: var(--orange);
  }
  .brand-name {
    font-weight: 400;
    font-size: 28px;
    color: var(--ink);
    line-height: 1.1;
  }
  .section { position: absolute; left: 30px; }
  .section.occurrence { top: 196px; }
  .section.looks { top: 334px; }
  .section h2 {
    margin: 0 0 9px;
    font-family: "Source Serif 4", serif;
    font-weight: 700;
    font-size: 24px;
    color: var(--orange-text);
    line-height: 1.3;
  }
  .section p {
    margin: 0;
    font-size: 22.5px;
    line-height: 25.8px;
  }
  .section p span { display: block; white-space: nowrap; }
  .fun-fact {
    position: absolute;
    left: 0; top: 623px;
    width: 1029px; height: 105px;
    background: var(--orange);
    color: #fff;
  }
  .fun-fact-label {
    position: absolute;
    left: 30px; top: 24px;
    margin: 0;
    font-family: "Source Serif 4", serif;
    font-weight: 800;
    font-size: 42px;
    line-height: 1.2;
  }
  .fun-fact-text {
    position: absolute;
    left: 272px; top: 18px;
    margin: 0;
    font-weight: 600;
    font-size: 27.5px;
    line-height: 32.5px;
    white-space: nowrap;
  }
</style>
</head>
<body>
  <article class="poster">
    <div class="photo" role="img" aria-label="Foto: drei Unzertrennliche, zwei grüne mit rotem Kopf und einer türkisblauer mit hellem Kopf, sitzen auf einem schrägen Ast vor Holzwand"></div>
    <div class="title-box"><h1 class="title">UNZERTRENNLICHE</h1></div>

    <section class="info">
      <div class="brand">
        <span class="brand-dot"></span>
        <span class="brand-name">Wildpark Kernbachtal</span>
      </div>
      <div class="section occurrence">
        <h2>Vorkommen:</h2>
        <p><span>Unzertrennliche leben in Afrika sowohl in</span><span>heißen Savannen als auch in</span><span>feucht-tropischen Regenwäldern.</span></p>
      </div>
      <div class="section looks">
        <h2>Aussehen:</h2>
        <p><span>Ihre Farbgebung gibt den verschiede-</span><span>nen Arten ihren Namen. Es gibt</span><span>Grauköpfchen, Orangeköpfchen, Taran-</span><span>tapapageien, Grünköpfchen, Rosenköpf-</span><span>chen, Pfirsichköpfchen, Schwarzköpf-</span><span>chen, Erdbeerköpfchen und Rußköpf-</span><span>chen. Unzertrennliche werden rund 13</span><span>bis 18 Zentimeter lang und wiegen etwa</span><span>50 Gramm</span></p>
      </div>
    </section>

    <footer class="fun-fact">
      <p class="fun-fact-label">FUN FACT :</p>
      <p class="fun-fact-text">Wussten Sie, das Unzertrennliche im Englischen „Lovebirds“<br>(übersetzt: „Liebesvögel“) heißen?</p>
    </footer>
  </article>
</body>
</html>
```